Business Card Colourful and fun Design Project

I need a business card design for my Ecommerce website which am launching soon. we are based in the United Arab Emirates and our customers are based in Dubai and other cities in UAE, In addition to our neighbour countries in the GCC. We sell Gadgets, fashion and other trendy stuff that are hard to find in our market. The company name is "ZIMTOWALRUS" logo consists of a panda wearing traditional local Arab thobe. would like to see a clean, colourful fun design to represent us.
Updates
please read the discussion board. thanks
Industry/Entity Type
Fashion
Look and feel
Each slider illustrates characteristics of the customer's brand and the style your logo design should communicate.

```html
<!DOCTYPE html>
<html lang="en">
<head>
<meta charset="utf-8">
<title>ZIMTOWALRUS Business Card</title>
<link href="https://fonts.googleapis.com/css2?family=Arimo:wght@400;700&display=swap" rel="stylesheet">
<style>
  :root {
    --brand-red: #a8141d;
    --paper: #ffffff;
    --canvas-bg: #ecebe8;
    --ink: #3a3a3a;
    --rule: #9a9a9a;
    --fig-light: #f1f1f1;
    --fig-mid: #c9c9c9;
  }
  * { box-sizing: border-box; margin: 0; padding: 0; }
  html, body { width: 1146px; height: 1200px; overflow: hidden; }
  body {
    background: var(--canvas-bg);
    font-family: "Arimo", Arial, sans-serif;
    position: relative;
  }
  .card {
    position: absolute;
    left: 123px;
    width: 900px;
    height: 514px;
    overflow: hidden;
    box-shadow: 0 6px 18px rgba(0,0,0,.18);
  }
  .card--front { top: 57px; background: var(--brand-red); color: var(--paper); }
  .card--back { top: 628px; background: var(--paper); color: var(--ink); }

  /* Front */
  .mascot-area {
    position: absolute;
    left: 80px; top: 110px;
    width: 290px; height: 370px;
    border-radius: 40px;
    background: radial-gradient(ellipse at 50% 40%, var(--fig-light) 0%, var(--fig-mid) 70%, rgba(201,201,201,0) 100%);
  }
  .front-info {
    position: absolute;
    right: 60px; top: 50px;
    text-align: right;
  }
  .wordmark {
    font-weight: 700;
    letter-spacing: 1px;
    white-space: nowrap;
  }
  .front-info .wordmark { font-size: 48px; color: var(--paper); margin-bottom: 22px; }
  .person-name { font-size: 32px; font-weight: 700; letter-spacing: 1px; }
  .job-title { font-size: 20px; font-weight: 700; margin-top: 6px; }
  .contact-list { list-style: none; margin-top: 30px; }
  .contact-list li {
    display: flex; justify-content: flex-end; align-items: center;
    gap: 12px; font-size: 22px; font-weight: 700; margin-bottom: 14px;
  }
  .contact-icon { width: 24px; height: 24px; fill: var(--paper); }

  /* Back */
  .back-brand {
    position: absolute; right: 70px; top: 40px;
    display: flex; align-items: flex-end; gap: 18px;
  }
  .mascot-mini {
    width: 70px; height: 80px; border-radius: 14px;
    background: radial-gradient(ellipse at 50% 40%, #f4f4f4 0%, #cfcfcf 75%, rgba(207,207,207,0) 100%);
  }
  .back-brand .wordmark { font-size: 32px; color: var(--brand-red); margin-bottom: 6px; }
  .notes {
    position: absolute; left: 60px; top: 150px; right: 70px;
  }
  .notes-label {
    position: absolute; left: 0; top: 0;
    font-size: 20px; font-weight: 700; color: var(--brand-red); letter-spacing: 1px;
  }
  .note-line {
    position: absolute; right: 0; height: 0;
    border-top: 2px dashed var(--rule);
  }
  .socials {
    position: absolute; left: 60px; bottom: 40px;
    list-style: none;
  }
  .socials li, .social-right {
    display: flex; align-items: center; gap: 16px;
    font-size: 28px; font-weight: 700; color: var(--ink);
    margin-top: 14px;
  }
  .social-right { position: absolute; right: 70px; top: 346px; margin: 0; font-size: 24px; }
  .social-mark {
    width: 28px; height: 28px; border-radius: 4px; background: var(--brand-red); flex: none;
  }
</style>
</head>
<body>
  <section class="card card--front">
    <div class="mascot-area" role="img" aria-label="Brand mascot illustration"></div>
    <div class="front-info">
      <div class="wordmark">ZIMTOWALRUS</div>
      <div class="person-name">YOUR NAME</div>
      <div class="job-title">JOB TITLE</div>
      <ul class="contact-list">
        <li>800 ZIMTO (94686)
          <svg class="contact-icon" viewBox="0 0 24 24" aria-hidden="true"><path d="M3 8c0-2 4-4 9-4s9 2 9 4v2h-5V8H8v2H3zM6 11h12l2 8H4z"/></svg>
        </li>
        <li>123Address
          <svg class="contact-icon" viewBox="0 0 24 24" aria-hidden="true"><path d="M12 2a7 7 0 0 0-7 7c0 5 7 13 7 13s7-8 7-13a7 7 0 0 0-7-7zm0 9.5A2.5 2.5 0 1 1 12 6.5a2.5 2.5 0 0 1 0 5z"/></svg>
        </li>
        <li>UAE<span style="width:24px"></span></li>
      </ul>
    </div>
  </section>

  <section class="card card--back">
    <div class="back-brand">
      <div class="mascot-mini" role="img" aria-label="Small brand mascot illustration"></div>
      <div class="wordmark">ZIMTOWALRUS</div>
    </div>
    <div class="notes">
      <span class="notes-label">NOTES.</span>
      <div class="note-line" style="top:20px; left:90px;"></div>
      <div class="note-line" style="top:70px; left:0;"></div>
      <div class="note-line" style="top:120px; left:0;"></div>
      <div class="note-line" style="top:170px; left:0;"></div>
    </div>
    <div class="social-right"><span class="social-mark"></span>@zimtowalrusuae</div>
    <ul class="socials">
      <li><span class="social-mark"></span>zimtowalrus.ae/page</li>
      <li><span class="social-mark"></span>zimtowalrusuae</li>
    </ul>
  </section>
</body>
</html>
```